Clean business card with logo provided

I want a card that will stand out among the masses. I need the color and image to show professionalism and yet have a family appeal showing that I only deal with win/win scenarios. The back of the card will be used to take notes about the individual so I can use that in my database entry. I like modern design but need professionalism in it also. It needs to fit my "clean, safe, and affordable housing" motto. I need to be able to write on the file and update the card details for my employees.

Target Market(s)

Investors looking to make investment income through real estate

Industry/Entity Type

Real Estate

Contact Information for Business Card

Mark Dunthorpe
blank address, city, st, zip code
480-555-3174
markdunthorpe@brivoholdings.example
www.brivoholdings.example

Font styles to use
Sans Serif

Requirements
Must have
• I would like the back of the card to have lines for info. example
• Met/Visited: Date:
• Interets:
Nice to have
• I want the cards color to match the logo background color. Font with details to be san serif and black. I want the card rectangular with square corners. Standard business card size. I would like to see cards designed with both images to see which i prefer more.

```html
<!DOCTYPE html>
<html lang="en">
<head>
<meta charset="utf-8">
<title>Tarnwell Leasing LLC – Business Cards</title>
<link href="https://fonts.googleapis.com/css2?family=Raleway:wght@400;500&display=swap" rel="stylesheet">
<style>
  :root {
    --bg: #d4d6d9;
    --teal: #1db4cb;
    --teal-deep: #159fb8;
    --ink: #0a0b0c;
    --paper: #ffffff;
    --rule: #c9ccd0;
    --muted: #9aa0a6;
    --light: #e6f7fa;
  }
  * { box-sizing: border-box; margin: 0; padding: 0; }
  html, body { width: 1200px; height: 1000px; overflow: hidden; }
  body {
    background: radial-gradient(circle at 50% 40%, #eceef0 0%, var(--bg) 75%);
    font-family: "Raleway", sans-serif;
    position: relative;
  }
  .card {
    position: absolute;
    width: 500px;
    height: 286px;
    overflow: hidden;
    box-shadow: 0 14px 30px rgba(0,0,0,0.18);
  }
  .card--dark-front { left: 80px;  top: 180px; background: var(--ink); }
  .card--back-a     { left: 620px; top: 180px; }
  .card--back-b     { left: 80px;  top: 530px; }
  .card--teal-front { left: 620px; top: 530px; background: linear-gradient(135deg, var(--teal), var(--teal-deep)); }

  .band { position: absolute; left: 0; right: 0; height: 12px; }
  .band--top { top: 0; }
  .band--bottom { bottom: 0; }
  .card--dark-front .band { background: var(--teal); }
  .card--teal-front .band,
  .card--back .band { background: var(--ink); }

  .brand {
    position: absolute;
    top: 70px; left: 0; right: 0;
    text-align: center;
  }
  .brand__name {
    display: inline-flex;
    align-items: center;
    gap: 12px;
    font-size: 30px;
    font-weight: 500;
    letter-spacing: 2px;
    white-space: nowrap;
  }
  .brand__dot { width: 18px; height: 18px; border-radius: 50%; flex: none; }
  .card--dark-front .brand__name { color: var(--teal); }
  .card--dark-front .brand__dot { background: var(--teal); }
  .card--teal-front .brand__name { color: var(--paper); }
  .card--teal-front .brand__dot { background: var(--ink); }
  .brand__motto {
    margin-top: 10px;
    font-size: 12px;
    letter-spacing: 0.5px;
  }
  .card--dark-front .brand__motto { color: var(--teal); }
  .card--teal-front .brand__motto { color: var(--ink); }

  .contact {
    position: absolute;
    left: 20px; right: 20px; bottom: 44px;
    display: flex;
    justify-content: space-between;
    align-items: flex-start;
    font-size: 8px;
    line-height: 1.9;
    white-space: nowrap;
  }
  .contact__name { font-size: 11px; line-height: 1.4; }
  .contact__group { padding-left: 9px; border-left: 1px solid; }
  .card--dark-front .contact { color: var(--muted); }
  .card--dark-front .contact__group { border-color: #3b3f43; }
  .card--teal-front .contact { color: var(--light); }
  .card--teal-front .contact__group { border-color: rgba(255,255,255,0.4); }

  .card--back { background: var(--paper); }
  .notes { position: absolute; inset: 0; font-size: 13px; color: var(--ink); }
  .notes__date {
    position: absolute; top: 40px; right: 28px;
    display: flex; align-items: flex-end; gap: 8px;
    font-size: 11px;
  }
  .notes__date .line { width: 120px; flex: none; }
  .notes__fields {
    position: absolute; left: 36px; right: 36px; top: 110px;
    display: flex; flex-direction: column; gap: 20px;
  }
  .field { display: flex; align-items: flex-end; gap: 10px; }
  .field__label { white-space: nowrap; }
  .line { flex: 1; border-bottom: 1px solid var(--rule); height: 14px; }
</style>
</head>
<body>

<section class="card card--dark-front" aria-label="Card front, black">
  <div class="band band--top"></div>
  <div class="brand">
    <div class="brand__name">Tarnwell Leasing LLC <span class="brand__dot"></span></div>
    <p class="brand__motto">Providing clean, safe, and affordable housing</p>
  </div>
  <div class="contact">
    <div class="contact__name">Mark Dunthorpe</div>
    <div class="contact__group">480-555-3174<br>markdunthorpe@brivoholdings.example</div>
    <div class="contact__group">Blank address, city, st, zip code<br>www.brivoholdings.example</div>
  </div>
  <div class="band band--bottom"></div>
</section>

<section class="card card--back card--back-a" aria-label="Card back, notes">
  <div class="band band--top"></div>
  <div class="notes">
    <div class="notes__date">Date: <span class="line"></span></div>
    <div class="notes__fields">
      <div class="field"><span class="field__label">Met/Visited:</span><span class="line"></span></div>
      <div class="field"><span class="field__label">Interets:</span><span class="line"></span></div>
      <div class="field"><span class="field__label">Problems:</span><span class="line"></span></div>
    </div>
  </div>
  <div class="band band--bottom"></div>
</section>

<section class="card card--back card--back-b" aria-label="Card back, notes">
  <div class="band band--top"></div>
  <div class="notes">
    <div class="notes__date">Date: <span class="line"></span></div>
    <div class="notes__fields">
      <div class="field"><span class="field__label">Met/Visited:</span><span class="line"></span></div>
      <div class="field"><span class="field__label">Interets:</span><span class="line"></span></div>
      <div class="field"><span class="field__label">Problems:</span><span class="line"></span></div>
    </div>
  </div>
  <div class="band band--bottom"></div>
</section>

<section class="card card--teal-front" aria-label="Card front, teal">
  <div class="band band--top"></div>
  <div class="brand">
    <div class="brand__name">Tarnwell Leasing LLC <span class="brand__dot"></span></div>
    <p class="brand__motto">Providing clean, safe, and affordable housing</p>
  </div>
  <div class="contact">
    <div class="contact__name">Mark Dunthorpe</div>
    <div class="contact__group">480-555-3174<br>markdunthorpe@brivoholdings.example</div>
    <div class="contact__group">Blank address, city, st, zip code<br>www.brivoholdings.example</div>
  </div>
  <div class="band band--bottom"></div>
</section>

</body>
</html>
```